Wordpress Design Papa Academy Project

Need a homepage design for a wordpress site that is based around becoming a better Dad. The sitemap file and logo file are attached. Navigation should be a combination of horizontal and vertical because the sitemap is extensive. I think the Father's conference, Daddy daughter dance and Essay contest would like nice if they were highlighted in their own rounded boxes at the bottom of the home page perhaps. New design needs to be attention grabbing, colorful but not over the top or too flashy either. I would like the background to be pictures and/or transparent words(similar to this site http://kinhelm.com/). Need a banner image which will be a slider and I need text overlay at the bottom of each image. I like rounded boxes like how this site showcases the news and events sections - http://www.qt.edu/. Need to also incorporate an events calendar, facebook and twitter icons and contact info. A preliminary design was initially created and is attached for you to review. Design needs to be balanced as there is alot of info to display.I have a current site here http://www.papaacad.com/ and you will see why I need a new design.
Updates

Target Market(s)

Dads

Industry/Entity Type

Events

Requirements
Must have
• image slider with text overlay on image, combination of horizontal and vertical navigation, show a dropdown menu under one of the horizontal tabs, events calendar, web safe fonts, colorful, use stock images for any placeholders,footer with sitemap
Nice to have
• rounded boxes, highlight father's conference,daddy daughter dance and essay contest in a separate section from the navigation, also put campus book store and online classes in a vertical nav bar perhaps - maybe in bigger placeholders like stacked boxes or similar.

```html
<!DOCTYPE html>
<html lang="en">
<head>
<meta charset="utf-8">
<title>Papa Academy, Inc. – Home</title>
<link rel="stylesheet" href="https://fonts.googleapis.com/css2?family=Oswald:wght@400;500&family=Arimo:wght@400;700&family=Tinos&display=swap">
<style>
:root{
  --navy:#0b1a3c;
  --navy-2:#122650;
  --ink:#1d3160;
  --text:#333a45;
  --muted:#5a6270;
  --page:#e4e5e7;
  --panel:#ffffff;
  --panel-mid:#efefef;
  --rule:#cfd2d6;
  --red:#c8102e;
  --green:#8bc53f;
  --blue-box:#0d4f8f;
  --link-blue:#2a5a9a;
}
*{box-sizing:border-box;margin:0;padding:0}
html,body{width:1054px;height:1200px;overflow:hidden}
body{position:relative;background:linear-gradient(#dfe0e2,#ebecee 40%,#e4e5e7);font-family:Arimo,Arial,sans-serif;color:var(--text)}
.abs{position:absolute}

/* header */
.site-header{left:0;top:0;width:1054px;height:102px;background:var(--navy);border-bottom:2px solid #2b3c63}
.brand{left:18px;top:18px;display:flex;align-items:center;gap:18px}
.brand-mark{width:68px;height:68px;border-radius:50%;background:#3b5488}
.brand-name{font-family:Tinos,Georgia,serif;font-size:30px;color:#fff;white-space:nowrap}
.top-links{right:30px;top:7px;display:flex;list-style:none;font-size:13px;color:#fff;white-space:nowrap}
.top-links li{padding:0 9px;border-left:1px solid #7c88a5;line-height:14px}
.top-links li:first-child{border-left:0}
.search{left:780px;top:45px;width:203px;height:30px;border-radius:15px;background:#fff;font-size:13px;color:#222;padding:7px 16px}
.search-go{left:990px;top:45px;width:31px;height:31px;border-radius:50%;background:var(--red);color:#fff;font-size:11px;font-weight:700;text-align:center;line-height:31px}

/* side navigation */
.side-nav{left:12px;top:125px;width:187px;height:403px;background:var(--navy);border-radius:5px;border:2px solid #2d3d63;padding:16px 0}
.side-nav::before,.side-nav::after{content:"";position:absolute;left:6px;right:6px;height:4px;border-top:1px dashed #596a92}
.side-nav::before{top:6px}.side-nav::after{bottom:6px}
.side-nav ul{list-style:none}
.side-nav li{height:40px;line-height:40px;text-align:center;font-family:Oswald,sans-serif;font-size:16px;color:#fff;margin:0 30px;border-bottom:1px dashed #44557c;white-space:nowrap}
.side-nav li:last-child{border-bottom:0}

/* slider */
.slider{left:230px;top:125px;width:801px;height:397px;border-radius:5px;border:4px solid #fff;overflow:hidden;box-shadow:0 0 3px rgba(0,0,0,.25)}
.slider-art{position:absolute;inset:0;background:
  radial-gradient(circle at 25% 40%,#f2a21d 0,#e8452c 18%,transparent 40%),
  radial-gradient(circle at 45% 70%,#2eaadc 0,#7b3fa0 22%,transparent 45%),
  radial-gradient(circle at 60% 20%,#8cc63f 0,transparent 25%),
  linear-gradient(90deg,#d94a8c 0,#8e3fa8 30%,#dcdcdc 62%,#f4f4f4 100%)}
.slider-title{left:424px;top:90px;font-size:33px;color:var(--ink);letter-spacing:.5px;white-space:nowrap}
.slider-arrow{width:45px;height:41px;border-radius:8px;background:var(--green);top:181px}
.slider-arrow svg{display:block;margin:10px auto}
.slider-arrow.prev{left:11px}.slider-arrow.next{left:736px}
.slider-caption{left:33px;top:275px;width:351px;height:82px;background:rgba(40,40,48,.72);padding:7px 14px;color:#fff}
.slider-caption h3{font-family:Oswald,sans-serif;font-size:15px;font-weight:400;line-height:19px;text-decoration:underline;color:#fff6c8;white-space:nowrap}
.slider-caption p{font-size:12.5px;line-height:16px;margin-top:1px}
.slider-caption a{color:#ffe98a;text-decoration:underline}

/* content panel */
.content{left:12px;top:556px;width:1021px;height:700px;background:var(--panel);border-radius:6px;border:1px solid #c9cbcf;overflow:hidden}
.col-mid{left:469px;top:0;width:305px;height:100%;background:var(--panel-mid);border-left:1px dashed var(--rule);border-right:1px dashed var(--rule)}
.col-mid-body{left:469px;top:0;width:305px;height:100%}

/* posts */
.post-tab{left:-8px;width:441px;height:46px;background:var(--navy)}
.post-tab::before{content:"";position:absolute;inset:5px 5px 5px 10px;border:1px dashed #a9b4cc}
.post-tab::after{content:"";position:absolute;left:0;bottom:-7px;border-top:7px solid #6d0f1d;border-left:8px solid transparent}
.post-tab h2{position:absolute;left:46px;top:9px;font-family:Oswald,sans-serif;font-weight:400;font-size:19px;color:#fff;white-space:nowrap}
.post-text{left:38px;width:400px;font-size:12px;line-height:16px;color:#333}
.read-more{left:284px;width:135px;height:30px;border-radius:15px;background:linear-gradient(#fafafa,#dedede);border:1px solid #cfcfcf;font-size:12.5px;text-align:center;line-height:28px;color:#222}

/* section headings */
.col-head{font-family:Oswald,sans-serif;font-size:17px;color:var(--navy);white-space:nowrap}
.col-head span{color:#9aa0a8;font-size:13px;margin-left:8px}

/* events */
.event{left:34px;width:260px;height:45px}
.event-date{position:absolute;left:0;top:0;width:35px;height:45px;background:#fff;border:1px solid #c4c8ce;text-align:center}
.event-date .mon{display:block;background:#5e7bb0;color:#fff;font-size:8px;line-height:10px}
.event-date .day{display:block;font-size:15px;line-height:18px;color:#222}
.event-date .wd{display:block;font-size:8px;color:#555}
.event-box{position:absolute;left:42px;top:5px;width:211px;min-height:25px;background:#fff;border:1px solid #c9ccd1;border-radius:3px;font-size:12.5px;line-height:14px;padding:5px 6px;color:var(--link-blue)}
.event-box b{color:#222;margin-right:4px}
.view-cal{left:192px;top:442px;width:90px;height:18px;border:1px solid #b8bcc2;border-radius:3px;background:#fff;font-size:10px;line-height:16px;text-align:center;color:#222;white-space:nowrap}
.hr{height:0;border-top:1px dashed var(--rule)}
.fact{left:20px;width:270px;font-size:12.5px;line-height:16px;color:#333}

/* right column */
.social{left:812px;display:flex;gap:8px}
.social i{display:block;width:34px;height:34px;border-radius:6px}
.essay-box{left:794px;top:268px;width:207px;height:136px;background:var(--blue-box);border:2px solid #0a3c70}
.essay-box li{list-style:none;height:44px;border-bottom:1px solid #3d73ac;color:#fff;font-size:12.5px;line-height:15px;padding:0 14px;display:flex;align-items:center}
.essay-box li:last-child{border-bottom:0}
.video{left:794px;top:503px;width:204px;height:200px;background:linear-gradient(#3a3f44,#1c1e21)}
.video-play{position:absolute;left:74px;top:56px;width:56px;height:38px;border-radius:8px;background:rgba(0,0,0,.7)}
</style>
</head>
<body>

<header class="site-header abs">
  <div class="brand abs"><div class="brand-mark"></div><span class="brand-name">Papa Academy, Inc.</span></div>
  <ul class="top-links abs"><li>Home</li><li>Contact Us</li><li>Terms of Use</li><li>Site Map</li><li>Privacy Policy</li><li>Advertising</li></ul>
  <div class="search abs">Search</div>
  <div class="search-go abs">GO</div>
</header>

<nav class="side-nav abs">
  <ul>
    <li>Home</li><li>About » »</li><li>Admissions » »</li><li>Information » »</li><li>Products » »</li><li>Online Courses</li><li>Blog » »</li><li>Contact Us</li>
  </ul>
</nav>

<section class="slider abs">
  <div class="slider-art" role="img" aria-label="Colourful abstract illustration of glossy tiles, circles and ribbons promoting online courses"></div>
  <div class="slider-title abs">ONLINE COURSES</div>
  <div class="slider-arrow prev abs"><svg width="14" height="20" viewBox="0 0 14 20"><path d="M11 2 3 10l8 8" fill="none" stroke="#fff" stroke-width="3"/></svg></div>
  <div class="slider-arrow next abs"><svg width="14" height="20" viewBox="0 0 14 20"><path d="M3 2l8 8-8 8" fill="none" stroke="#fff" stroke-width="3"/></svg></div>
  <div class="slider-caption abs">
    <h3>A Diverse and Interesting Array of Online Courses</h3>
    <p>Browse through our diverse range of online courses and start changing your life as a father, today! <a>Read More</a></p>
  </div>
</section>

<main class="content abs">
  <div class="col-mid abs"></div>

  <div class="post-tab abs" style="top:26px"><h2>More news on a post here</h2></div>
  <p class="post-text abs" style="top:80px">more interesting information about your latest news will appear here as a 'news flash'</p>
  <div class="read-more abs" style="top:125px">Read More</div>

  <div class="post-tab abs" style="top:192px"><h2>Another interesting post</h2></div>
  <p class="post-text abs" style="top:252px">your text for the post will appear here</p>
  <div class="read-more abs" style="top:280px">Read More</div>

  <div class="post-tab abs" style="top:347px"><h2>Fatherhood Statistics</h2></div>
  <p class="post-text abs" style="top:405px">Here is where the information about Fatherhood Statistics will appear as an excerpt of the entire post regarding this subject ...</p>
  <div class="read-more abs" style="top:452px">Read More</div>

  <div class="post-tab abs" style="top:519px"><h2>College of Parenting</h2></div>
  <p class="post-text abs" style="top:577px">Details about the parenting studies can be found on this post .</p>
  <div class="read-more abs" style="top:608px">Read More</div>

  <div class="col-mid-body abs">
    <div class="col-head abs" style="left:22px;top:49px">Upcoming Events<span>»</span></div>
    <div class="event abs" style="top:84px"><div class="event-date"><span class="mon">DEC</span><span class="day">10</span><span class="wd">Mon</span></div><div class="event-box"><b>7:30 am</b>Father Son Day</div></div>
    <div class="event abs" style="top:135px"><div class="event-date"><span class="mon">DEC</span><span class="day">30</span><span class="wd">Sun</span></div><div class="event-box"><b>7:45 am</b>Lecture: Teenage Years</div></div>
    <div class="event abs" style="top:187px"><div class="event-date"><span class="mon">JAN</span><span class="day">18</span><span class="wd">Fri</span></div><div class="event-box"><b>5:45 am</b>Daddy Daughter Dance</div></div>
    <div class="event abs" style="top:238px"><div class="event-date"><span class="mon">JAN</span><span class="day">31</span><span class="wd">Thu</span></div><div class="event-box"><b>5:45 am</b>Father's Conference</div></div>
    <div class="event abs" style="top:290px"><div class="event-date"><span class="mon">FEB</span><span class="day">14</span><span class="wd">Thu</span></div><div class="event-box"><b>5:45 am</b>Essay Contest Winners Lunch</div></div>
    <div class="event abs" style="top:341px"><div class="event-date"><span class="mon">MAR</span><span class="day">22</span><span class="wd">Fri</span></div><div class="event-box"><b>5:45 am</b>Father and Child Golf Day</div></div>
    <div class="event abs" style="top:393px"><div class="event-date"><span class="mon">APR</span><span class="day">7</span><span class="wd">Sun</span></div><div class="event-box"><b>5:45 am</b>Father and Son Basketball Tournament</div></div>
    <div class="view-cal abs">View Calendar ➔</div>
    <div class="hr abs" style="left:0;top:479px;width:305px"></div>
    <div class="col-head abs" style="left:20px;top:527px">MM Did You Know?<span>»</span></div>
    <p class="fact abs" style="top:574px">5 out of 6 parents experience (fill in your own facts here) ..........</p>
    <p class="fact abs" style="top:622px">1 in 5 fathers has a concern about (fill in your</p>
  </div>

  <div class="col-head abs" style="left:794px;top:49px">Papa Academy Social Side<span>»</span></div>
  <div class="social abs" style="top:87px"><i style="background:#3fa9e0"></i><i style="background:#3b5998"></i><i style="background:#d84a38"></i><i style="background:#1b75b1"></i></div>
  <div class="social abs" style="top:132px"><i style="background:#f08a24"></i><i style="background:#6ab344"></i><i style="background:#8a9bb8"></i></div>
  <div class="hr abs" style="left:774px;top:189px;width:247px"></div>
  <div class="col-head abs" style="left:794px;top:235px">ESSAY CONTEST<span>»</span></div>
  <ul class="essay-box abs"><li>My Hero / My Dad Essay Contest</li><li>Essay Submission</li><li>Picture Gallery</li></ul>
  <div class="hr abs" style="left:774px;top:438px;width:247px"></div>
  <div class="col-head abs" style="left:794px;top:470px">Tutorial Video Library<span>»</span></div>
  <div class="video abs" role="img" aria-label="Tutorial video still with a parenting clip">
    <div class="video-play"><svg width="56" height="38" viewBox="0 0 56 38"><path d="M22 11v16l14-8z" fill="#fff"/></svg></div>
  </div>
</main>

</body>
</html>
```